Fun relaxed Travel Photography Business Card*

Require a fun, funky and quirky but rememberable business card for a travel photographer

Industry/Entity Type

Photographer

Contact Information for Business Card

Front Card

(my name) Tavo M.

Travel Photographer ( small under travel photographer) “self-proclaimed”

(website logo) wanderingtavo.example

(PhotoFeed logo) @wandering_with_tavo

(PhotoFeed logo) @wandering_with_tavo_2.0 (backup for when PhotoFeed puts Tavo on timeout for bad behaviour)

Tel: N/A (removing the potential awkwardness of me not replying)

Email: (see above)

Back Card

Offending people since 1986

(Bottom right corner) “p.s. travelling made me fatTER”

Font styles to use
Serif

Colors

Designer to choose colors to be used in the design.

Requirements
Must have
• a camera
• a similar cartoon version of me as the "logo" see attached files, try to make as similar as possible

```html
<!DOCTYPE html>
<html lang="en">
<head>
<meta charset="utf-8">
<title>Tavo M. – Travel Photographer Business Card</title>
<link href="https://fonts.googleapis.com/css2?family=Arimo:wght@400;700&family=Quattrocento:wght@400&display=swap" rel="stylesheet">
<style>
  :root {
    --sheet: #ffffff;
    --ink: #111111;
    --white: #ffffff;
    --card-red: #e50914;
    --card-orange: #ef8a00;
    --card-lime: #8fd400;
    --card-green: #4fc21c;
    --back-black: #000000;
    --face-tint: rgba(255, 255, 255, 0.28);
    --face-tint-dark: #2a2a2a;
  }
  * { box-sizing: border-box; margin: 0; padding: 0; }
  html, body {
    width: 1104px; height: 1200px; overflow: hidden;
    background: var(--sheet);
  }
  .sheet { position: relative; width: 1104px; height: 1200px; }

  .card {
    position: absolute; left: 213px; width: 678px; height: 387px;
    overflow: hidden;
  }
  .card-front {
    top: 142px;
    background: linear-gradient(to top right,
      var(--card-red) 28%, var(--card-orange) 52%, var(--card-lime) 78%, var(--card-green) 100%);
    color: var(--white);
    font-family: "Arimo", Arial, sans-serif;
  }
  .card-back {
    top: 629px;
    background: var(--back-black);
    color: var(--white);
  }

  .side-label {
    position: absolute; left: 0; width: 1104px; text-align: center;
    font-family: "Arimo", Arial, sans-serif; font-size: 29px; color: var(--ink);
  }
  .side-label.front { top: 553px; }
  .side-label.back { top: 1032px; }

  /* front */
  .camera-icon { position: absolute; left: 154px; top: 32px; width: 60px; height: 46px; }
  .identity { position: absolute; left: 0; width: 368px; text-align: center; }
  .name { top: 86px; font-size: 35px; }
  .role { top: 129px; font-size: 26px; }
  .role-note { top: 161px; font-size: 19px; }

  .contacts { position: absolute; left: 32px; top: 199px; font-weight: 700; font-size: 18px; }
  .contact { display: flex; align-items: center; height: 29px; }
  .contact svg { width: 18px; height: 18px; margin-right: 3px; flex: none; }
  .contact-note { padding-left: 21px; font-size: 15.5px; line-height: 24px; margin: 3px 0 1px; }

  .portrait-front {
    position: absolute; left: 368px; top: 22px; width: 292px; height: 344px;
    border-radius: 46% 46% 48% 48% / 40% 40% 60% 60%;
    background: var(--face-tint);
    border: 3px solid var(--white);
  }

  /* back */
  .portrait-back {
    position: absolute; left: 278px; top: 68px; width: 124px; height: 146px;
    border-radius: 46% 46% 48% 48% / 40% 40% 60% 60%;
    background: var(--face-tint-dark);
    border: 2px solid var(--white);
  }
  .tagline {
    position: absolute; left: 0; top: 222px; width: 678px; text-align: center;
    font-family: "Quattrocento", Georgia, serif; font-size: 39px; letter-spacing: 1px;
  }
  .postscript {
    position: absolute; right: 14px; top: 350px;
    font-family: "Arimo", Arial, sans-serif; font-weight: 700; font-size: 26px;
  }
</style>
</head>
<body>
<div class="sheet">

  <section class="card card-front">
    <svg class="camera-icon" viewBox="0 0 60 46" fill="none" stroke="#fff" stroke-width="2.5">
      <rect x="2" y="5" width="56" height="39" rx="9"/>
      <rect x="42" y="1" width="10" height="5" rx="1.5"/>
      <circle cx="30" cy="24" r="13"/>
      <circle cx="30" cy="24" r="7"/>
    </svg>
    <h1 class="identity name" style="font-weight:400">Tavo M.</h1>
    <p class="identity role">Travel Photographer</p>
    <p class="identity role-note">“self-proclaimed”</p>

    <div class="contacts">
      <div class="contact">
        <svg viewBox="0 0 18 18" fill="none" stroke="#fff" stroke-width="1.6"><circle cx="9" cy="9" r="7.5"/><path d="M1.5 9h15M9 1.5c-4 4.5-4 10.5 0 15M9 1.5c4 4.5 4 10.5 0 15"/></svg>
        wanderingtavo.example
      </div>
      <div class="contact">
        <svg viewBox="0 0 18 18" fill="none" stroke="#fff" stroke-width="1.6"><rect x="1.5" y="1.5" width="15" height="15"/></svg>
        @wandering_with_tavo
      </div>
      <div class="contact">
        <svg viewBox="0 0 18 18" fill="none" stroke="#fff" stroke-width="1.6"><rect x="1.5" y="1.5" width="15" height="15"/></svg>
        @wandering_with_tavo_2.0
      </div>
      <p class="contact-note">(backup for when PhotoFeed puts Tavo<br>on timeout for bad behaviour)</p>
      <div class="contact">
        <svg viewBox="0 0 18 18" fill="none" stroke="#fff" stroke-width="1.6"><rect x="1" y="3.5" width="16" height="11"/><path d="M1 3.5l8 6 8-6"/></svg>
        Email:
      </div>
    </div>

    <div class="portrait-front" role="img" aria-label="Cartoon portrait logo of Tavo with round hibiscus sunglasses and a beard"></div>
  </section>
  <p class="side-label front">FRONT</p>

  <section class="card card-back">
    <div class="portrait-back" role="img" aria-label="Small cartoon portrait logo of Tavo with round sunglasses"></div>
    <p class="tagline">Offending people since 1986</p>
    <p class="postscript">“p.s. travelling made me fatTER”</p>
  </section>
  <p class="side-label back">BACK</p>

</div>
</body>
</html>
```